Pull Up Banner - Recruitment Company

We would like a design for a pull up banner.

For context: we are a recruitment business. We specialise in helping people in healthcare industry to find jobs in Australia.

I have come up with several ideas and text for the banner. Feel free to use the following as you see appropriate:

- Our logo (see attached)
- 'Healthcare Recruitment Agency'
- Some sort of imagine / cartoon of medical professionals (ie. doctor, nurse, physiotherapist, speech pathologist). A cartoon is more friendly than committing to a photo
- 'Empowering your next career move'
- 'Discover tailored opportunities based on your career preferences'
- Dot points (allied health, nursing, medical imaging)
- Contact info at the bottom including our website (www.pellatalent.com.au, our Instagram handle @pellatalent, Mobile: XXXX XXX XXX. The title section for contact information could be 'Get in touch:'

Feel free to submit a couple of designs and we can merge aspects that look good on your designs and find the perfect fit.
Thank you
Updates

Hello,

Thank you for your initial submissions to this project. I appreciate the time you've invested.

After reviewing the first attempt, I'd like to share some feedback and initial observations:

- Professionalism and engagement: Is the overall appearance of the banner professional? It's crucial that we have a high-quality design as this will represent our business.

- Image selection: The image (whether cartoon or real people) appears quite generic. Please consider submitting the banner with a few different photos in the middle for us to choose from. Ensure the image is a good fit and not simply a generic stock photo.

- Contact section: Kindly remove the phone number; we no longer wish to include it on the banner. Instead, please include our website (www.pellatalent.com.au) and Instagram handle (@pellatalent).

- Color scheme: White, black, and red/pink are preferred, or alternatively, blue. However, please avoid incorporating too many different colors as it may detract from the professional appearance.

We will be printing the design on a banner and require it to look professional and engaging.

Thank you once again for your submissions. I hope the feedback provided above is helpful.

Warm regards,

Target Market(s)

Allied Health Australia

Font styles to use
Serif

Colors
0054AA
0677BA
7BADD7
CADEEF
E8F1F8
0094D4
00A9DD
6FCCEA
C7EBF8
E9F6FB
EB3D1F
EC4F4E
F09395
F8D3D4
FCEDEE

```html
<!DOCTYPE html>
<html lang="en">
<head>
<meta charset="utf-8">
<title>Pella Talent – Pull Up Banner</title>
<link href="https://fonts.googleapis.com/css2?family=Open+Sans:wght@400;600;700;800&display=swap" rel="stylesheet">
<style>
  :root {
    --page-bg: #e9edf2;
    --banner-bg: #f3f5f9;
    --header-bg: #d6dce5;
    --ink: #0d0f14;
    --brand-blue: #1f35a8;
    --accent-blue: #2c3fb0;
    --figure-tone-a: #e3e7ee;
    --figure-tone-b: #c9d2de;
    --white: #ffffff;
  }
  * { box-sizing: border-box; margin: 0; padding: 0; }
  html, body {
    width: 1200px;
    height: 900px;
    overflow: hidden;
    background: var(--page-bg);
    font-family: "Open Sans", Arial, sans-serif;
  }
  .canvas {
    position: relative;
    width: 1200px;
    height: 900px;
    display: flex;
    justify-content: center;
    align-items: center;
  }
  .banner {
    position: relative;
    width: 376px;
    height: 870px;
    background: linear-gradient(180deg, #eef1f6 0%, var(--white) 100%);
    box-shadow: 0 6px 24px rgba(30, 45, 80, 0.15);
    display: flex;
    flex-direction: column;
    align-items: center;
    text-align: center;
    color: var(--ink);
  }
  .banner-header {
    width: 100%;
    height: 114px;
    background: var(--header-bg);
    display: flex;
    align-items: center;
    justify-content: center;
  }
  .brand-name {
    font-weight: 800;
    font-size: 38px;
    letter-spacing: 3px;
    color: var(--ink);
    text-transform: uppercase;
  }
  .tagline {
    margin-top: 34px;
    font-weight: 700;
    font-size: 18px;
    line-height: 1.4;
    color: var(--brand-blue);
    text-transform: uppercase;
  }
  .headline {
    margin-top: 24px;
    font-weight: 800;
    font-size: 56px;
    line-height: 0.92;
    letter-spacing: 0.5px;
    text-transform: uppercase;
  }
  .subline {
    margin-top: 12px;
    font-weight: 400;
    font-size: 26px;
    line-height: 1.28;
    text-transform: uppercase;
  }
  .highlight {
    margin-top: 6px;
    display: inline-block;
    background: var(--accent-blue);
    color: var(--white);
    font-weight: 800;
    font-size: 42px;
    line-height: 1.05;
    padding: 0 4px;
    text-transform: uppercase;
  }
  .closing {
    font-weight: 400;
    font-size: 37px;
    line-height: 1.15;
    text-transform: uppercase;
  }
  .team-illustration {
    margin-top: 20px;
    width: 100%;
    height: 262px;
    background: radial-gradient(ellipse at 50% 50%, var(--figure-tone-a) 0%, var(--figure-tone-b) 75%, transparent 76%);
  }
  .contact {
    margin-top: 22px;
    display: flex;
    flex-direction: column;
    align-items: center;
    gap: 6px;
  }
  .website {
    font-weight: 600;
    color: var(--ink);
    font-size: 14px;
  }
  .website .domain { font-size: 23px; font-weight: 600; }
  .handle {
    font-weight: 700;
    font-size: 21px;
    color: var(--accent-blue);
  }
</style>
</head>
<body>
  <main class="canvas">
    <section class="banner">
      <header class="banner-header">
        <span class="brand-name">Pella Talent</span>
      </header>

      <p class="tagline">Healthcare<br>Recruitment Agency</p>

      <h1 class="headline">Discover<br>Tailored</h1>
      <p class="subline">Opportunities<br>based on</p>
      <p class="highlight">Your Career</p>
      <p class="closing">Preferences</p>

      <div class="team-illustration" role="img" aria-label="Illustration of three medical professionals in white coats standing together"></div>

      <footer class="contact">
        <p class="website">www.<span class="domain">pellatalent</span>.com.au</p>
        <p class="handle">@pellatalent</p>
      </footer>
    </section>
  </main>
</body>
</html>
```